Fore Sale sign for my real estate agency

I am a Brisbane - Australia inner western suburbs boutique real estate agent who is needing a for sale sign. We are a small dynamic family agency that needs a for sale sign that will standout and give us a strong presence in the market.

I have attached a logo I like, however I am not fixed on anything and am open to suggestions.

The information on the sign should contain but not necessarily limited to the following information - please appreciate I am very open
1 logo - Vellman
2 Ph number - 3847 1593
3 web address - vellman.example.au

Thank you
Glen Vellman

```html
<!DOCTYPE html>
<html lang="en">
<head>
<meta charset="utf-8">
<title>Vellman – For Sale Sign</title>
<link rel="stylesheet" href="https://fonts.googleapis.com/css2?family=Archivo:wdth,wght@62..125,400;62..125,700;62..125,800&display=swap">
<style>
  :root {
    --orange: #f7981d;
    --orange-soft: #f9b866;
    --ink: #111111;
    --white: #ffffff;
    --backdrop: #e4e4e4;
  }
  * { margin: 0; padding: 0; box-sizing: border-box; }
  html, body {
    width: 1200px;
    height: 1200px;
    overflow: hidden;
    background: var(--backdrop);
  }
  .sign {
    position: absolute;
    left: 50px;
    top: 187px;
    width: 1100px;
    height: 826px;
    background: var(--white);
    overflow: hidden;
    font-family: "Archivo", Arial, sans-serif;
  }
  .sign-edge {
    position: absolute;
    left: 0;
    top: 0;
    width: 180px;
    height: 826px;
  }
  .brand-name {
    position: absolute;
    left: 120px;
    top: 60px;
    width: 930px;
    text-align: center;
    font-size: 225px;
    line-height: 1;
    font-weight: 800;
    font-stretch: 100%;
    color: var(--ink);
    letter-spacing: 0;
    white-space: nowrap;
  }
  .sale-banner {
    position: absolute;
    left: 152px;
    top: 421px;
    width: 910px;
    height: 104px;
    background: var(--orange);
    color: var(--white);
    font-size: 118px;
    font-weight: 700;
    font-stretch: 125%;
    line-height: 104px;
    text-align: center;
    letter-spacing: 16px;
    padding-left: 16px;
    white-space: nowrap;
  }
  .phone {
    position: absolute;
    left: 152px;
    top: 542px;
    width: 910px;
    text-align: center;
    font-size: 146px;
    font-weight: 800;
    font-stretch: 125%;
    line-height: 1;
    color: var(--ink);
    letter-spacing: 8px;
    white-space: nowrap;
  }
  .web {
    position: absolute;
    left: 152px;
    top: 668px;
    width: 910px;
    text-align: center;
    font-size: 70px;
    font-weight: 400;
    font-stretch: 118%;
    line-height: 1;
    color: var(--ink);
    letter-spacing: 5px;
    white-space: nowrap;
  }
  .pattern-strip {
    position: absolute;
    left: 152px;
    top: 748px;
    width: 910px;
    height: 54px;
    background: var(--orange-soft);
  }
</style>
</head>
<body>
  <main class="sign">
    <svg class="sign-edge" viewBox="0 0 180 826" aria-hidden="true">
      <rect x="0" y="0" width="106" height="826" fill="var(--orange)"/>
      <rect x="113" y="0" width="9" height="826" fill="var(--ink)"/>
      <circle cx="168" cy="200" r="130" fill="var(--white)"/>
    </svg>
    <div class="brand-name">Vellman</div>
    <div class="sale-banner">FOR SALE</div>
    <div class="phone">3847 1593</div>
    <div class="web">vellman.example.au</div>
    <div class="pattern-strip" role="img" aria-label="Row of small orange checker squares as a decorative border"></div>
  </main>
</body>
</html>
```